Create a basic website for a new air cargo consultancy, called 'Veltrane Loadwise'

We want to build a basic website (homepage, 'about us' page, services and contact us page).
We have a logo, we have most of the text to be inserted, but not all. We also still need to take pictures.
We would like to have a fresh and modern, but business like design and the creation of the website.
We want to be able to modify the website after (add pictures and more text, update references).
We already have a url.

```html
<!DOCTYPE html>
<html lang="en">
<head>
<meta charset="utf-8">
<title>Veltrane Loadwise</title>
<link href="https://fonts.googleapis.com/css2?family=Poppins:wght@400;500;600;700&display=swap" rel="stylesheet">
<style>
:root{
  --blue:#2e3896;
  --blue-deep:#283189;
  --blue-soft:#dfe1ef;
  --gold:#d4a02a;
  --ink:#111111;
  --grey-text:#666a73;
  --field:#f2f2f2;
  --white:#ffffff;
  --black:#000000;
}
*{box-sizing:border-box;margin:0;padding:0}
html,body{width:1200px;height:3665px;overflow:hidden}
body{position:relative;font-family:'Poppins',sans-serif;background:var(--white);color:var(--ink)}
.abs{position:absolute}
.btn{position:absolute;background:var(--gold);color:var(--white);font-weight:600;text-transform:uppercase;border-radius:4px;display:flex;align-items:center;justify-content:center;font-size:17px}

/* header */
.site-header{position:absolute;left:0;top:0;width:1200px;height:88px;background:var(--white)}
.brand{position:absolute;left:47px;top:30px;color:var(--gold);font-weight:600;font-size:22px;display:flex;align-items:center;gap:8px}
.brand-dot{width:12px;height:12px;border-radius:50%;background:var(--gold)}
.nav a{position:absolute;top:41px;font-size:15px;color:var(--ink);text-decoration:none}
.header-btn{left:1013px;top:36px;width:141px;height:31px;font-size:14px}

/* hero */
.hero-photo{position:absolute;left:0;top:88px;width:1200px;height:652px;background:linear-gradient(180deg,#7d7f86 0%,#5f6269 45%,#3f4249 100%);clip-path:polygon(0 0,100% 0,100% 88%,0 100%)}
.hero-wedge{position:absolute;left:0;top:0;width:1200px;height:760px}
.hero-panel{position:absolute;left:0;top:196px;width:648px;height:331px;background:rgba(46,56,150,.82);clip-path:polygon(0 22%,100% 0,100% 100%,0 100%)}
.hero-title{position:absolute;left:77px;top:296px;color:var(--white);font-weight:600;font-size:58px;letter-spacing:.5px;line-height:1}
.hero-text{position:absolute;left:76px;top:380px;width:500px;color:var(--white);font-size:14.5px;line-height:17px}
.hero-btn{left:75px;top:437px;width:167px;height:37px}

/* section heads */
.section-head{position:absolute;display:flex;align-items:center;gap:10px;font-weight:600;font-size:30px;text-transform:uppercase}
.swoosh{width:136px;height:22px}

/* about */
.about-frame{position:absolute;left:-6px;top:970px;width:588px;height:285px;border:5px solid var(--blue);border-left:none}
.about-photo{position:absolute;left:104px;top:855px;width:428px;height:372px;background:linear-gradient(160deg,#c9ccd2 0%,#8c8f95 55%,#4b4e57 100%)}
.about-text{position:absolute;left:650px;top:994px;width:478px;font-size:13px;line-height:22px;color:var(--grey-text)}
.about-btn{left:648px;top:1127px;width:179px;height:43px}

/* services */
.services-bg{position:absolute;left:0;top:1354px;width:1200px;height:877px;background:var(--blue-soft)}
.services-shape{position:absolute;left:0;top:1354px;width:1200px;height:877px}
.service{position:absolute;top:1638px;width:226px;text-align:center}
.service-ring{width:226px;height:226px;border-radius:50%;background:rgba(255,255,255,.12);display:flex;align-items:center;justify-content:center}
.service-disc{width:186px;height:186px;border-radius:50%;background:var(--white);display:flex;align-items:center;justify-content:center}
.service-disc svg{width:104px;height:104px;fill:none;stroke:var(--blue);stroke-width:3;stroke-linecap:round;stroke-linejoin:round}
.service-name{position:absolute;top:1896px;width:280px;text-align:center;color:var(--white);font-weight:600;font-size:17px}
.services-btn{left:510px;top:2010px;width:180px;height:43px}

/* contact */
.field{position:absolute;background:var(--field);border-radius:6px;color:#444;font-size:21px;padding:24px 0 0 35px}
.send-btn{left:510px;top:2949px;width:180px;height:43px}

/* footer */
.footer-shape{position:absolute;left:0;top:3100px;width:1200px;height:565px}
.footer-brand{position:absolute;left:114px;top:3340px;color:var(--gold);font-weight:600;font-size:38px;display:flex;align-items:center;gap:12px}
.footer-brand .brand-dot{width:18px;height:18px}
.footer-about{position:absolute;left:109px;top:3440px;width:330px;color:var(--white);font-size:13px;line-height:16px}
.footer-title{position:absolute;top:3320px;color:var(--gold);font-weight:600;font-size:24px}
.footer-link{position:absolute;left:553px;color:var(--white);font-size:14px;display:flex;align-items:center;gap:8px}
.footer-link svg{width:30px;height:10px}
.footer-contact{position:absolute;left:855px;color:var(--white);font-size:15px;display:flex;align-items:center;gap:14px}
.footer-contact svg{width:22px;height:22px;fill:var(--gold)}
.copyright{position:absolute;left:0;top:3620px;width:1200px;text-align:center;color:var(--white);font-size:12.5px}
</style>
</head>
<body>

<svg width="0" height="0" style="position:absolute">
  <defs>
    <symbol id="swoosh" viewBox="0 0 136 22">
      <path d="M0 4 C40 6 90 8 136 9 L136 14 C90 13 40 10 0 4Z" fill="#d4a02a"/>
      <path d="M10 9 C50 12 95 15 136 16 L136 21 C95 20 50 16 10 9Z" fill="#d4a02a"/>
    </symbol>
    <symbol id="mini-swoosh" viewBox="0 0 30 10">
      <path d="M0 1 C10 2 20 3 30 3 L30 5 C20 5 10 4 0 1Z M4 5 C14 6 22 7 30 7 L30 9 C22 9 14 8 4 5Z" fill="#d4a02a"/>
    </symbol>
  </defs>
</svg>

<header class="site-header">
  <div class="brand"><span class="brand-dot"></span>Veltrane Loadwise</div>
  <nav class="nav">
    <a style="left:423px">HOME</a>
    <a style="left:525px">ABOUT</a>
    <a style="left:634px">SERVICES</a>
    <a style="left:758px">BLOG</a>
  </nav>
  <div class="btn header-btn">Contact Us</div>
</header>

<section class="hero">
  <div class="hero-photo" role="img" aria-label="Passenger jets parked at an airport apron at dusk"></div>
  <svg class="hero-wedge" viewBox="0 0 1200 760"><polygon points="915,666 1200,643 1200,743" fill="var(--blue)"/></svg>
  <div class="hero-panel"></div>
  <h1 class="hero-title">VELTRANE LOADWISE</h1>
  <p class="hero-text">Welcome to Veltrane Loadwise, your premier consultancy specialized in the air cargo sector.</p>
  <div class="btn hero-btn">Contact Us</div>
</section>

<section class="about">
  <div class="about-frame"></div>
  <div class="about-photo" role="img" aria-label="Two business travellers walking through an airport terminal"></div>
  <h2 class="section-head" style="left:650px;top:912px"><svg class="swoosh"><use href="#swoosh"/></svg>About Us</h2>
  <p class="about-text">Welcome to Veltrane Loadwise, your premier consultancy specialized in the air cargo sector. We are dedicated to helping clients enhance their overall cargo strategy, drive digital transformation, foster community building, and achieve sustainability goals.</p>
  <div class="btn about-btn">Read More</div>
</section>

<section class="services">
  <div class="services-bg"></div>
  <svg class="services-shape" viewBox="0 0 1200 877" role="img" aria-label="Team working together, shown under a blue overlay">
    <polygon points="0,69 608,0 1200,62 1200,793 608,877 0,807" fill="var(--blue)"/>
  </svg>
  <h2 class="section-head" style="left:420px;top:1497px;color:var(--white)"><svg class="swoosh"><use href="#swoosh"/></svg>Our Services</h2>

  <div class="service" style="left:83px"><div class="service-ring"><div class="service-disc">
    <svg viewBox="0 0 100 100"><rect x="14" y="18" width="58" height="44"/><line x1="43" y1="12" x2="43" y2="18"/><line x1="36" y1="62" x2="28" y2="80"/><line x1="50" y1="62" x2="58" y2="80"/><rect x="24" y="46" width="6" height="10"/><rect x="34" y="40" width="6" height="16"/><rect x="44" y="44" width="6" height="12"/><polyline points="22,36 32,30 42,34 54,26"/><circle cx="66" cy="50" r="11"/><line x1="74" y1="58" x2="84" y2="70"/></svg>
  </div></div></div>
  <div class="service" style="left:357px"><div class="service-ring"><div class="service-disc">
    <svg viewBox="0 0 100 100"><path d="M50 18 A32 32 0 1 0 50 82"/><path d="M50 30 A20 20 0 1 0 50 70"/><line x1="50" y1="40" x2="72" y2="30"/><line x1="50" y1="50" x2="80" y2="50"/><line x1="50" y1="60" x2="72" y2="70"/><circle cx="75" cy="29" r="3"/><circle cx="83" cy="50" r="3"/><circle cx="75" cy="71" r="3"/></svg>
  </div></div></div>
  <div class="service" style="left:630px"><div class="service-ring"><div class="service-disc">
    <svg viewBox="0 0 100 100"><circle cx="50" cy="50" r="11"/><circle cx="26" cy="24" r="9"/><circle cx="74" cy="28" r="6"/><circle cx="20" cy="58" r="5"/><circle cx="34" cy="78" r="7"/><circle cx="74" cy="74" r="9"/><line x1="33" y1="31" x2="42" y2="42"/><line x1="69" y1="32" x2="58" y2="42"/><line x1="25" y1="57" x2="39" y2="52"/><line x1="38" y1="72" x2="44" y2="60"/><line x1="58" y1="58" x2="67" y2="67"/></svg>
  </div></div></div>
  <div class="service" style="left:903px"><div class="service-ring"><div class="service-disc">
    <svg viewBox="0 0 100 100"><circle cx="46" cy="56" r="28"/><path d="M26 40 C34 44 36 52 44 52 C50 60 42 70 46 82"/><path d="M56 30 C54 40 64 46 72 44"/><path d="M66 36 C66 22 78 14 90 14 C90 28 82 38 66 36Z"/></svg>
  </div></div></div>

  <div class="service-name" style="left:56px">STRATEGIC PLANNING</div>
  <div class="service-name" style="left:331px">DIGITALIZATION</div>
  <div class="service-name" style="left:610px">COMMUNITY BUILDING</div>
  <div class="service-name" style="left:882px">SUSTAINABILITY</div>

  <div class="btn services-btn">View Services</div>
</section>

<section class="contact">
  <h2 class="section-head" style="left:398px;top:2346px"><svg class="swoosh"><use href="#swoosh"/></svg>Contact Us</h2>
  <div class="field" style="left:203px;top:2465px;width:385px;height:77px">Name</div>
  <div class="field" style="left:613px;top:2465px;width:385px;height:77px">Email</div>
  <div class="field" style="left:203px;top:2564px;width:385px;height:78px">Phone Number</div>
  <div class="field" style="left:613px;top:2564px;width:385px;height:78px">Subject</div>
  <div class="field" style="left:203px;top:2673px;width:795px;height:208px">Your Message</div>
  <div class="btn send-btn">Send Now</div>
</section>

<footer>
  <svg class="footer-shape" viewBox="0 0 1200 565">
    <polygon points="420,62 1200,22 1200,107" fill="#cfcfcf"/>
    <polygon points="0,37 1200,107 1200,565 0,565" fill="var(--black)"/>
  </svg>
  <div class="footer-brand"><span class="brand-dot"></span>Veltrane Loadwise</div>
  <p class="footer-about">Welcome to Veltrane Loadwise, your premier consultancy specialized in the air cargo sector.</p>

  <div class="footer-title" style="left:552px">Quick Links</div>
  <div class="footer-link" style="top:3378px"><svg><use href="#mini-swoosh"/></svg>HOME</div>
  <div class="footer-link" style="top:3418px"><svg><use href="#mini-swoosh"/></svg>ABOUT</div>
  <div class="footer-link" style="top:3456px"><svg><use href="#mini-swoosh"/></svg>SERVICES</div>
  <div class="footer-link" style="top:3496px"><svg><use href="#mini-swoosh"/></svg>BLOG</div>

  <div class="footer-title" style="left:851px">Contact Info</div>
  <div class="footer-contact" style="top:3386px"><svg viewBox="0 0 24 24"><path d="M6.6 10.8c1.4 2.8 3.8 5.1 6.6 6.6l2.2-2.2c.3-.3.7-.4 1-.2 1.1.4 2.3.6 3.6.6.6 0 1 .4 1 1V20c0 .6-.4 1-1 1C10.6 21 3 13.4 3 4c0-.6.4-1 1-1h3.5c.6 0 1 .4 1 1 0 1.3.2 2.5.6 3.6.1.3 0 .7-.2 1z"/></svg>(+00)555 010 246</div>
  <div class="footer-contact" style="top:3433px"><svg viewBox="0 0 24 24"><path d="M3 9 12 3l9 6v11H3z M3 9l9 6 9-6"/></svg>support@veltrane.example</div>
  <div class="footer-contact" style="top:3478px"><svg viewBox="0 0 24 24"><path d="M12 2C8.1 2 5 5.1 5 9c0 5.2 7 13 7 13s7-7.8 7-13c0-3.9-3.1-7-7-7zm0 9.5a2.5 2.5 0 1 1 0-5 2.5 2.5 0 0 1 0 5z"/></svg>Harbor Lane No.12, Eastport</div>

  <p class="copyright">Privacy Policy | © Copyright 2024, All Rights Reserved.</p>
</footer>

</body>
</html>
```